Postcard double sided

Title: DWAYNE'S REVENGE

Why would Dwayne Bettancourt align himself with Gerald Ostrander?

(photo of two guys)

Dwayne approached elected officials that he wanted to run for office, but did not have money to finance his campaign. He wanted other elected officials to finance his campaign. Everyone told him that they would help him get the vote out, but that he needed to finance his own race.

In comes Gerald Ostrander.

Gerald Ostrander who has a pay to play scheme over at the City, told Dwayne he would finance his campaign on one condition.

He needed to run against Dennis Varga.

Why would Dwayne want to run with no money?

Backside

DWAYNE'S REVENGE

Dwayne decided to run because no one on the school board would terminate Dwayne's ex and her new boyfriend who both work for the school district. His ex even filed criminal charges against him that are still pending.

Mug Shot facing left (name the charges Criminal Trespass , and Criminal Mischief (highlight bold letters use two lines) mug shot facing right

Complaint one (then photo with full face) Compliant 2)
(showcharges)

Dwayne's ultimate goal is to terminate his ex and her new boyfriend if elected.
Plus Gerald Ostrander needs the majority on the school board to do what he does bet.

Kickbacks for Contracts.

They will hire their own contractors!
Say "No" to Dwayne's Revenge and Gerald Ostrander Money Grab!

Title On Back: all caps: DOMESTIC VIOLENCE

```html
<!DOCTYPE html>
<html lang="en">
<head>
<meta charset="utf-8">
<title>Dwayne's Revenge – Postcard</title>
<link href="https://fonts.googleapis.com/css2?family=Lato:wght@400;700;900&family=Montserrat:ital,wght@1,800;1,900&display=swap" rel="stylesheet">
<style>
:root{
  --stage:#3c3c3e;
  --red:#c8202a;
  --red-dark:#a3151d;
  --navy:#14204f;
  --blue:#3e5aa8;
  --blue-light:#8ea2d6;
  --gold:#f0b429;
  --ink:#1b1b1f;
  --white:#ffffff;
  --paper:#f7f7f7;
  --photo-a:#5b6b8f;
  --photo-b:#2a3760;
  --mug:#9a9ca2;
}
*{margin:0;padding:0;box-sizing:border-box}
html,body{width:1200px;height:1200px;overflow:hidden}
body{background:var(--stage);position:relative;font-family:"Lato",sans-serif}
.card{position:absolute;top:197px;width:562px;height:728px;background:var(--white);overflow:hidden;box-shadow:0 8px 24px rgba(0,0,0,.45)}
.card--front{left:25px}
.card--back{left:610px;width:563px}
.abs{position:absolute}
.headline{font-family:"Montserrat",sans-serif;font-style:italic;font-weight:900;color:var(--white);text-align:center;white-space:nowrap}
.header-band{left:0;top:0;width:100%;background:linear-gradient(90deg,var(--red-dark),var(--red) 50%,var(--red-dark))}
.header-rule{left:0;width:100%;height:4px;background:var(--red)}

/* front */
.front-art{left:0;top:0}
.front-question{right:18px;top:68px;width:340px;text-align:right;font-weight:900;font-size:21px;line-height:20px;color:var(--ink);text-transform:uppercase}
.underline-red{border-bottom:3px solid var(--red)}
.front-body{left:19px;top:368px;width:420px;color:var(--white);font-size:14.6px;line-height:20px;font-weight:700}
.in-comes{left:19px;top:484px;color:var(--white);font-weight:900;font-size:20px;line-height:26px}
.in-comes .name{color:var(--gold);display:inline-block;padding-right:2px;border-bottom:3px solid var(--red)}
.front-condition{right:19px;top:532px;width:330px;text-align:right;color:var(--white);font-size:14.6px;line-height:22px;font-weight:700}
.front-condition .cond{border-bottom:2px solid var(--red);font-weight:900}
.front-box{left:98px;top:617px;width:385px;height:39px;background:var(--white);text-align:center;line-height:39px;font-weight:900;font-size:15px;color:var(--navy)}
.front-box .name{color:var(--red)}
.footer-band{left:0;bottom:0;width:100%;background:linear-gradient(90deg,var(--red-dark),var(--red) 50%,var(--red-dark))}

/* back */
.back-intro{left:0;top:52px;width:100%;text-align:center;font-weight:700;font-size:14.2px;line-height:18px;color:var(--ink)}
.mug-band{left:0;top:120px;width:100%;height:215px;background:var(--blue-light)}
.mug{background:linear-gradient(180deg,#b9bbc0,var(--mug));border:3px solid var(--white);box-shadow:0 2px 6px rgba(0,0,0,.35)}
.charge-stamp{left:160px;top:136px;width:260px;height:46px;background:var(--white);border:3px solid var(--red);box-shadow:0 2px 5px rgba(0,0,0,.3);text-align:center;color:var(--red);font-weight:900;font-size:16px;line-height:17px;padding-top:5px;text-transform:uppercase}
.docs{left:0;top:335px;width:100%;height:160px;background:var(--white)}
.doc{top:14px;height:138px;color:#222;font-size:5.2px;line-height:6.6px;font-family:"Lato",sans-serif}
.doc .row{display:flex;justify-content:space-between}
.doc p{margin-top:3px}
.doc .sig{margin-top:10px;display:flex;justify-content:space-between;align-items:flex-end}
.doc .sig span{display:block;width:90px;border-top:1px solid #333;padding-top:1px}
.doc .date{font-size:7px;font-style:italic;border-bottom:1px solid #333}
.back-blue{left:0;top:495px;width:100%;height:160px;background:linear-gradient(90deg,var(--blue),#4f69b6)}
.back-goal{left:0;top:510px;width:100%;text-align:center;color:var(--white);font-weight:700;font-size:13.6px;line-height:17px}
.kickbacks{left:15px;top:560px;font-family:"Montserrat",sans-serif;font-style:italic;font-weight:900;font-size:21px;color:var(--white);padding-right:4px;border-bottom:3px solid var(--red);line-height:28px}
.hire{left:13px;top:596px;color:var(--white);font-weight:700;font-size:15px}
.say-no{right:10px;top:599px;font-family:"Montserrat",sans-serif;font-style:italic;font-weight:900;font-size:35px;color:var(--red);white-space:nowrap}
</style>
</head>
<body>

<!-- FRONT -->
<section class="card card--front">
  <svg class="abs front-art" width="562" height="728" viewBox="0 0 562 728">
    <defs>
      <linearGradient id="photoTone" x1="0" y1="0" x2="1" y2="1">
        <stop offset="0" stop-color="var(--photo-a)"/>
        <stop offset="1" stop-color="var(--photo-b)"/>
      </linearGradient>
      <linearGradient id="navyFade" x1="0" y1="0" x2="0" y2="1">
        <stop offset="0" stop-color="#14204f" stop-opacity="0"/>
        <stop offset="1" stop-color="#14204f" stop-opacity="1"/>
      </linearGradient>
    </defs>
    <rect x="0" y="48" width="562" height="6" fill="var(--red)"/>
    <polygon points="0,92 562,200 562,130 0,80" fill="var(--gold)"/>
    <polygon points="0,98 562,205 562,400 0,400" fill="url(#photoTone)" role="img" aria-label="Photo of Dwayne Bettancourt and Gerald Ostrander standing together in front of a campaign backdrop"/>
    <rect x="0" y="290" width="562" height="90" fill="url(#navyFade)"/>
    <rect x="0" y="379" width="562" height="290" fill="var(--navy)"/>
    <polygon points="0,668 562,414 562,668" fill="var(--blue)"/>
  </svg>

  <div class="abs header-band" style="height:48px"></div>
  <div class="abs headline" style="left:0;top:2px;width:100%;font-size:40px;line-height:46px">DWAYNE'S REVENGE</div>

  <div class="abs front-question">Why would Dwayne Bettancourt align himself with <span class="underline-red">Gerald Ostrander?</span></div>

  <div class="abs front-body">Dwayne approached elected officials that he wanted to run for office, but did not have money to finance his campaign. He wanted other elected officials to finance his campaign. Everyone told him that they would help him get the vote out, but that he needed to finance his own race.</div>

  <div class="abs in-comes">IN COMES<br><span class="name">Gerald Ostrander.</span></div>

  <div class="abs front-condition">Gerald Ostrander who has a pay to play scheme over at the City, told Dwayne he would finance his campaign on <span class="cond">ONE CONDITION:</span></div>

  <div class="abs front-box">HE NEEDED TO RUN AGAINST <span class="name">DENNIS VARGA</span></div>

  <div class="abs footer-band" style="height:59px"></div>
  <div class="abs headline" style="left:0;bottom:6px;width:100%;font-size:19px;line-height:20px">WHY WOULD DWAYNE WANT TO RUN<br>WITH NO MONEY?</div>
</section>

<!-- BACK -->
<section class="card card--back">
  <div class="abs header-band" style="height:43px"></div>
  <div class="abs headline" style="left:0;top:1px;width:100%;font-size:31px;line-height:42px">DOMESTIC VIOLENCE</div>
  <div class="abs header-rule" style="top:46px"></div>

  <div class="abs back-intro">Dwayne decided to run because no one on the school board would terminate<br>Dwayne's ex and her new boyfriend who both work for the school district.<br>His ex even filed criminal charges against him that are still pending.</div>

  <div class="abs mug-band"></div>
  <div class="abs mug" style="left:30px;top:135px;width:101px;height:123px" role="img" aria-label="Booking photo, profile facing left"></div>
  <div class="abs mug" style="left:233px;top:193px;width:99px;height:123px" role="img" aria-label="Booking photo, facing front"></div>
  <div class="abs mug" style="left:438px;top:135px;width:101px;height:123px" role="img" aria-label="Booking photo, profile facing right"></div>
  <div class="abs charge-stamp">Criminal Trespass<br>&amp; Criminal Mischief</div>

  <div class="abs docs"></div>
  <div class="abs doc" style="left:14px;top:349px;width:240px">
    <div class="row"><span>THE STATE OF TEXAS<br>COUNTY OF BRAZOS RIDGE</span><span>CR-19-15864-F</span></div>
    <p>IN THE NAME AND BY AUTHORITY OF THE STATE OF TEXAS:</p>
    <p>Before me, the undersigned assistant attorney, appeared the affiant, who under oath says the following is true.</p>
    <p>DWAYNE BETTANCOURT, on or about the 28th day of September, 2019, did intentionally enter property of Marisol Keene without her consent.</p>
    <p>AGAINST THE PEACE AND DIGNITY OF THE STATE.</p>
    <div class="sig"><span>Sworn to and subscribed before me on</span><em class="date">12-18-2019</em></div>
    <div class="sig"><span></span><span>Assistant Criminal District Attorney</span></div>
  </div>
  <div class="abs" style="left:262px;top:349px;width:1px;height:138px;background:#bbb"></div>
  <div class="abs doc" style="left:272px;top:349px;width:278px">
    <div class="row"><span>THE STATE OF TEXAS<br>COUNTY OF BRAZOS RIDGE</span><span>CR-19-15863-F</span></div>
    <p>IN THE NAME AND BY AUTHORITY OF THE STATE OF TEXAS:</p>
    <p>Before me, the undersigned assistant attorney, appeared the affiant, who under oath says the following is true.</p>
    <p>DWAYNE BETTANCOURT, on or about the 28th day of September, 2019, did knowingly damage garage lights owned by Marisol Keene.</p>
    <p>AGAINST THE PEACE AND DIGNITY OF THE STATE.</p>
    <div class="sig"><span>Sworn to and subscribed before me on</span><em class="date">12-18-2019</em></div>
    <div class="sig"><span></span><span>Assistant Criminal District Attorney</span></div>
  </div>

  <div class="abs back-blue"></div>
  <div class="abs back-goal">Dwayne's ultimate goal is to terminate his ex and her new boyfriend if elected.<br>Plus Gerald Ostrander needs the majority on the school board to do what he does bet.</div>
  <div class="abs kickbacks">Kickbacks for Contracts.</div>
  <div class="abs hire">They will hire their own contractors!</div>

  <svg class="abs" style="left:0;top:0" width="563" height="728" viewBox="0 0 563 728">
    <polygon points="318,655 350,588 563,588 563,655" fill="var(--white)"/>
  </svg>
  <div class="abs say-no">Say "No"</div>

  <div class="abs footer-band" style="top:648px;height:80px"></div>
  <div class="abs header-rule" style="top:648px;background:var(--white);height:3px"></div>
  <div class="abs headline" style="left:0;top:660px;width:100%;font-size:24px;line-height:28px">to Dwayne's Revenge and<br>Gerald Ostrander Money Grab!</div>
</section>

</body>
</html>
```